Packaging Sleeve Design for Yoghurt Tubs

Wagglenook makes frozen yoghurt treats for dogs. Our healthy treats are packaged like regular yoghurt in small tubs with a lid.

What we require is a design for our packaging using all the current logos and flavor icons we already have available.

The packaging will be a carton sleeve that wraps around the tubs.

We would like to maintain a wholesome / homemade look about the packaging following the design and look of our existing logo. You can visit the website www.wagglenook.com.au to get a better idea.

The packets will be displayed in a freezer so we would like something that will stand out to catch the customers eye.

Target Market(s)

Dog lovers, pet owners

Requirements
Must have
• Logo & flavours
All natural message
Low fat, low calories

```html
<!DOCTYPE html>
<html lang="en">
<head>
<meta charset="utf-8">
<title>Wagglenook – Yoghurt Tub Sleeve</title>
<link rel="stylesheet" href="https://fonts.googleapis.com/css2?family=Oswald:wght@400;500;700&display=swap">
<style>
  :root {
    --bg: #e6eef3;
    --orange: #f6a36b;
    --orange-light: #f9b786;
    --orange-deep: #f39a5e;
    --green: #9cc3ae;
    --green-light: #acd0bc;
    --green-deep: #92baa4;
    --ink: #1f2630;
    --white: #ffffff;
    --tub: #f4f2ee;
    --tub-shade: #d9d4cc;
    --mabel: #f2c992;
    --rocco: #a8c9e6;
    --daisy: #f5d84a;
    --oscar: #e27a2e;
    --lulu: #96d3c0;
  }
  * { box-sizing: border-box; margin: 0; padding: 0; }
  html, body { width: 1200px; height: 1190px; overflow: hidden; }
  body {
    background: var(--bg);
    font-family: "Oswald", "Arial Narrow", sans-serif;
    position: relative;
  }
  .sleeve {
    position: absolute;
    left: 40px;
    width: 1120px;
    height: 540px;
    border-radius: 6px;
    overflow: hidden;
    box-shadow: 0 4px 14px rgba(0,0,0,0.12);
  }
  .sleeve--filled { top: 30px; }
  .sleeve--outlined { top: 620px; }

  .top-panel {
    position: absolute;
    left: 0; top: 0;
    width: 100%; height: 230px;
  }
  .front-panel {
    position: absolute;
    left: 0; top: 230px;
    width: 100%; height: 310px;
  }
  .pattern {
    position: absolute;
    inset: 0;
  }
  .pattern--orange {
    background:
      radial-gradient(ellipse 60% 90% at 50% 40%, var(--orange-light), transparent 70%),
      linear-gradient(90deg, var(--orange-deep), var(--orange) 30%, var(--orange) 70%, var(--orange-deep));
  }
  .pattern--green {
    background:
      radial-gradient(ellipse 55% 80% at 50% 60%, var(--green-light), transparent 70%),
      linear-gradient(90deg, var(--green-deep), var(--green) 30%, var(--green) 70%, var(--green-deep));
  }

  .flavours {
    position: absolute;
    top: 24px;
    left: 0; right: 0;
    display: flex;
    justify-content: center;
    gap: 92px;
    list-style: none;
  }
  .flavour {
    width: 108px; height: 108px;
    border-radius: 50%;
    display: flex;
    flex-direction: column;
    align-items: center;
    justify-content: center;
    color: var(--white);
    text-align: center;
  }
  .flavour__name {
    font-size: 22px;
    font-weight: 700;
    letter-spacing: 0.5px;
    line-height: 1;
  }
  .flavour__taste {
    font-size: 8px;
    font-weight: 500;
    text-transform: uppercase;
    margin-top: 3px;
    letter-spacing: 0.3px;
  }
  .sleeve--filled .flavour--mabel { background: var(--mabel); }
  .sleeve--filled .flavour--rocco { background: var(--rocco); }
  .sleeve--filled .flavour--daisy { background: var(--daisy); }
  .sleeve--filled .flavour--oscar { background: var(--oscar); }
  .sleeve--filled .flavour--lulu { background: var(--lulu); }

  .sleeve--outlined .flavour { background: var(--white); }
  .sleeve--outlined .flavour--mabel { color: var(--oscar); }
  .sleeve--outlined .flavour--rocco { color: #6ea4d6; }
  .sleeve--outlined .flavour--daisy { color: #e8be12; }
  .sleeve--outlined .flavour--oscar { color: var(--oscar); }
  .sleeve--outlined .flavour--lulu { color: #5fbfa3; }

  .brand {
    position: absolute;
    top: 150px;
    left: 0; right: 0;
    display: flex;
    justify-content: center;
    align-items: center;
    gap: 12px;
    color: var(--ink);
  }
  .brand__dot {
    width: 54px; height: 54px;
    border-radius: 50%;
    background: var(--ink);
  }
  .brand__text { display: flex; flex-direction: column; }
  .brand__name {
    font-size: 34px;
    font-weight: 500;
    line-height: 1;
    letter-spacing: 1px;
  }
  .brand__claims {
    font-size: 11px;
    font-weight: 500;
    letter-spacing: 1.2px;
    text-transform: uppercase;
    margin-top: 4px;
  }

  .windows {
    position: absolute;
    left: 0; top: 0;
  }
</style>
</head>
<body>

<section class="sleeve sleeve--filled" aria-label="Sleeve with coloured flavour badges">
  <div class="top-panel">
    <div class="pattern pattern--orange" role="img" aria-label="Orange panel with a light outline pattern of apples, pumpkins, bananas, peanuts and chicken drumsticks"></div>
    <ul class="flavours">
      <li class="flavour flavour--mabel"><span class="flavour__name">MABEL</span><span class="flavour__taste">Peanut Butter</span></li>
      <li class="flavour flavour--rocco"><span class="flavour__name">ROCCO</span><span class="flavour__taste">Chicken &amp; Carrots</span></li>
      <li class="flavour flavour--daisy"><span class="flavour__name">DAISY</span><span class="flavour__taste">Banana</span></li>
      <li class="flavour flavour--oscar"><span class="flavour__name">OSCAR</span><span class="flavour__taste">Pumpkin</span></li>
      <li class="flavour flavour--lulu"><span class="flavour__name">LULU</span><span class="flavour__taste">Apple</span></li>
    </ul>
    <div class="brand">
      <span class="brand__dot"></span>
      <div class="brand__text">
        <span class="brand__name">Wagglenook</span>
        <span class="brand__claims">100% Natural · Low Fat · Low Calories</span>
      </div>
    </div>
  </div>
  <div class="front-panel">
    <div class="pattern pattern--green" role="img" aria-label="Sage green panel with a light outline pattern of apples, pumpkins, bananas, peanuts and chicken drumsticks"></div>
    <svg class="windows" width="1120" height="80" viewBox="0 0 1120 80" aria-hidden="true">
      <defs>
        <linearGradient id="tubA" x1="0" y1="0" x2="0" y2="1">
          <stop offset="0" stop-color="#d9d4cc"/>
          <stop offset="0.35" stop-color="#f4f2ee"/>
          <stop offset="1" stop-color="#ffffff"/>
        </linearGradient>
      </defs>
      <path d="M95 0 H300 V30 Q300 62 270 62 H125 Q95 62 95 30 Z" fill="url(#tubA)"/>
      <path d="M470 0 H690 V34 Q690 66 660 66 H500 Q470 66 470 34 Z" fill="url(#tubA)"/>
      <path d="M860 0 H1075 V30 Q1075 62 1045 62 H890 Q860 62 860 30 Z" fill="url(#tubA)"/>
    </svg>
  </div>
</section>

<section class="sleeve sleeve--outlined" aria-label="Sleeve with white flavour badges">
  <div class="top-panel">
    <div class="pattern pattern--orange" role="img" aria-label="Orange panel with a light outline pattern of apples, pumpkins, bananas, peanuts and chicken drumsticks"></div>
    <ul class="flavours">
      <li class="flavour flavour--mabel"><span class="flavour__name">MABEL</span><span class="flavour__taste">Peanut Butter</span></li>
      <li class="flavour flavour--rocco"><span class="flavour__name">ROCCO</span><span class="flavour__taste">Chicken &amp; Carrots</span></li>
      <li class="flavour flavour--daisy"><span class="flavour__name">DAISY</span><span class="flavour__taste">Banana</span></li>
      <li class="flavour flavour--oscar"><span class="flavour__name">OSCAR</span><span class="flavour__taste">Pumpkin</span></li>
      <li class="flavour flavour--lulu"><span class="flavour__name">LULU</span><span class="flavour__taste">Apple</span></li>
    </ul>
    <div class="brand">
      <span class="brand__dot"></span>
      <div class="brand__text">
        <span class="brand__name">Wagglenook</span>
        <span class="brand__claims">100% Natural · Low Fat · Low Calories</span>
      </div>
    </div>
  </div>
  <div class="front-panel">
    <div class="pattern pattern--green" role="img" aria-label="Sage green panel with a light outline pattern of apples, pumpkins, bananas, peanuts and chicken drumsticks"></div>
    <svg class="windows" width="1120" height="80" viewBox="0 0 1120 80" aria-hidden="true">
      <defs>
        <linearGradient id="tubB" x1="0" y1="0" x2="0" y2="1">
          <stop offset="0" stop-color="#d9d4cc"/>
          <stop offset="0.35" stop-color="#f4f2ee"/>
          <stop offset="1" stop-color="#ffffff"/>
        </linearGradient>
      </defs>
      <path d="M95 0 H300 V30 Q300 62 270 62 H125 Q95 62 95 30 Z" fill="url(#tubB)"/>
      <path d="M470 0 H690 V34 Q690 66 660 66 H500 Q470 66 470 34 Z" fill="url(#tubB)"/>
      <path d="M860 0 H1075 V30 Q1075 62 1045 62 H890 Q860 62 860 30 Z" fill="url(#tubB)"/>
    </svg>
  </div>
</section>

</body>
</html>
```